Clara Joy Fenwick- Lantern Harbour- Autumn/Winter Tour Dates

I need high res A3 Tour poster for print and for social media JPG sharing of tour dates.
Also needed Facebook/Twitter Banner Cover Photos of these dates.
Text Needed Below
Clara Joy Fenwick
Lantern Harbour
Autumn/Winter Tour Dates
03/09 Brackwell Folk Festival
21/09 Swindon- Tolmar Theatre
01/10 Hitchin- Pardock Folk Club
17/10 Bath- The Quill
20/10 Sheffield- Upper Gate Cricket Club
24/10 Birmingham- Copper Kettle Cafe
26/10 Glasgow- The Fox and Flagon
27/10 Edinburgh - The Marble Halls
08/11 Riverside Song and Dance Festival- The Wandering Heron
25/11 Lewes- Crescent Record Shop- Live In Store
02/12 Cambridge- The Platform
27/01 Lincolnshire- Darrowby Theatre
Tickets/Info: www.clarajoyfenwick-music.test/gigs
(Quotes/Reviews To Put On)
"Outstanding, rich and expressive."            "Vibrant and Experimental"
**** TnB                                                               **** Tunepaths
"Impressive and Invigorating"                        "Enchanting" Ballad Wireless UK
bLeaf

Updates
I cannot read the tour dates on most of the submissions so far. They need to be visible to viewers.
Thank You.
Please also be as creative and inventive as possible- not bland.

Target Market(s)
Music Fans- Folk Acoustic Americana
Industry/Entity Type
Media
Font styles to use
Requirements
Must have
- My photo featured prominently
- Look classy and not tacky or OTT
- Look elegant, wintery and eye catching
- The dates must be very clear to read
- Links to Website:

Nice to have
- Something innovative and not boring in terms of layout design
- Perhaps fading/ misty or wintery

Should not have
- Any colours that do not match

```html
<!DOCTYPE html>
<html lang="en">
<head>
<meta charset="utf-8">
<title>Clara Joy Fenwick – Lantern Harbour Tour Poster</title>
<link rel="stylesheet" href="https://fonts.googleapis.com/css2?family=Cormorant+SC:wght@500&family=Parisienne&family=Arimo:ital,wght@0,400;0,700;1,400&display=swap">
<style>
  :root {
    --night-deep: #0b1430;
    --night-mid: #1f2f5e;
    --mist: #3c5283;
    --frost: #9fcbe4;
    --snow: #ffffff;
    --date-text: #e4eaf4;
    --portrait-skin: #b9b6cc;
    --portrait-hair: #0c0f22;
  }
  * { margin: 0; padding: 0; box-sizing: border-box; }
  html, body { width: 873px; height: 1200px; overflow: hidden; background: var(--night-deep); }
  .poster {
    position: relative;
    width: 873px; height: 1200px;
    overflow: hidden;
    font-family: "Arimo", Arial, sans-serif;
    color: var(--snow);
  }
  .backdrop {
    position: absolute; inset: 0;
    background:
      radial-gradient(ellipse 60% 35% at 55% 18%, rgba(120,140,190,0.45), transparent 70%),
      radial-gradient(ellipse 55% 45% at 20% 40%, rgba(70,95,150,0.5), transparent 75%),
      linear-gradient(180deg, var(--night-mid) 0%, var(--mist) 35%, var(--night-mid) 65%, var(--night-deep) 100%);
  }
  .portrait {
    position: absolute;
    left: 420px; top: 300px; width: 453px; height: 900px;
    background:
      radial-gradient(ellipse 28% 22% at 48% 36%, var(--portrait-skin), transparent 75%),
      radial-gradient(ellipse 55% 60% at 50% 55%, var(--portrait-hair), transparent 80%);
    opacity: 0.9;
  }
  .artist-name {
    position: absolute; top: 38px; left: 0; width: 100%;
    text-align: center;
    font-family: "Cormorant SC", "Times New Roman", serif;
    font-weight: 500; font-size: 40px; letter-spacing: 1px;
  }
  .album-title {
    position: absolute; top: 108px; left: 60px; width: 813px;
    text-align: center;
    font-family: "Parisienne", cursive;
    font-size: 104px; line-height: 1.2;
  }
  .reviews { position: absolute; left: 35px; top: 312px; width: 400px; color: var(--frost); font-size: 18px; }
  .review { position: relative; text-align: center; }
  .review + .review { margin-top: 40px; }
  .review p { line-height: 1; margin-bottom: 19px; }
  .review .quote-line { font-style: italic; }
  .review .quote-line:first-child { text-align: left; padding-left: 45px; }
  .review .quote-line:first-child::before {
    content: "\201C"; position: absolute; left: 0; top: -8px;
    font-family: Georgia, serif; font-size: 44px; color: #7f9bb8; font-weight: 700;
  }
  .review .rating { font-style: normal; }
  .tour-heading { position: absolute; left: 33px; top: 628px; font-size: 22px; }
  .tour-dates { position: absolute; left: 32px; top: 672px; list-style: none; font-size: 17.5px; color: var(--date-text); }
  .tour-dates li { height: 28.2px; line-height: 28.2px; white-space: nowrap; }
  .tour-dates strong { font-weight: 700; color: var(--snow); }
  .tickets {
    position: absolute; top: 1126px; left: 0; width: 100%;
    text-align: center; font-size: 27px;
  }
  .tickets strong { font-weight: 700; }
</style>
</head>
<body>
<main class="poster">
  <div class="backdrop" role="img" aria-label="Misty midnight-blue wintry forest background with soft snowy sparkles"></div>
  <div class="portrait" role="img" aria-label="Portrait of the singer with long dark hair and a pearl crown, hand on chest"></div>

  <h1 class="artist-name">Clara Joy Fenwick</h1>
  <h2 class="album-title">Lantern Harbour</h2>

  <section class="reviews">
    <div class="review">
      <p class="quote-line">Outstanding, rich and expressive</p>
      <p class="quote-line">Vibrant and Experimental</p>
      <p class="rating">**** TnB **** Tunepaths</p>
    </div>
    <div class="review">
      <p class="quote-line">Impressive and Invigorating</p>
      <p class="quote-line">Enchanting</p>
      <p class="rating">**** Ballad Wireless UK</p>
    </div>
  </section>

  <h3 class="tour-heading">Autumn/Winter Tour Dates</h3>
  <ul class="tour-dates">
    <li>03/09 <strong>Brackwell Folk Festival</strong></li>
    <li>21/09 <strong>Swindon</strong> - Tolmar Theatre</li>
    <li>01/10 <strong>Hitchin</strong> - Pardock Folk Club</li>
    <li>17/10 <strong>Bath</strong> - The Quill</li>
    <li>20/10 <strong>Sheffield</strong> - Upper Gate Cricket Club</li>
    <li>24/10 <strong>Birmingham</strong> - Copper Kettle Cafe</li>
    <li>26/10 <strong>Glasgow</strong> - The Fox and Flagon</li>
    <li>27/10 <strong>Edinburgh</strong> - The Marble Halls</li>
    <li>08/11 <strong>Riverside Song and Dance Festival</strong></li>
    <li>- The Wandering Heron</li>
    <li>25/11 <strong>Lewes- Crescent Record Shop</strong>- Live In Store</li>
    <li>02/12 <strong>Cambridge</strong> - The Platform</li>
    <li>27/01 <strong>Lincolnshire</strong> - Darrowby Theatre</li>
  </ul>

  <p class="tickets">Tickets/Info: <strong>www.clarajoyfenwick-music.test/gigs</strong></p>
</main>
</body>
</html>
```